Creative Brief
Velor
NorthwindCoastal
Professional
Tobin R. Lestrade
President & Chief Development Officer
27340 SW Harrowgate Lane, Suite 240
Kirkland, Washington 98471
United States of America
tlestrade@velorhaulers.example
www.velorhaulers.example
Graphic design based on primary logo and web address.
We just had a logo upgrade done by QuillMarket. Please utilize this logo to submit entries. We are uploading this logo for you now.
Various Northwind Coastal logos in zip file.

```html
<!DOCTYPE html>
<html lang="en">
<head>
<meta charset="utf-8">
<title>Northwind Coastal Stationery</title>
<link href="https://fonts.googleapis.com/css2?family=Open+Sans:wght@400;600;700&display=swap" rel="stylesheet">
<style>
  :root{
    --backdrop:#e7e4df;
    --paper:#ffffff;
    --brand-red:#c1272d;
    --brand-red-dark:#9e1c22;
    --brand-navy:#1f2f5c;
    --ink:#555a63;
    --watermark:#eceef2;
  }
  *{box-sizing:border-box;margin:0;padding:0}
  html,body{width:1200px;height:734px;overflow:hidden}
  body{background:var(--backdrop);font-family:"Open Sans",Arial,sans-serif;color:var(--ink);position:relative}
  .sheet{position:absolute;background:var(--paper);box-shadow:0 2px 6px rgba(0,0,0,.18);overflow:hidden}
  .brand{display:flex;align-items:center;gap:6px;font-weight:700;color:var(--brand-navy);white-space:nowrap;letter-spacing:.02em}
  .brand-dot{border-radius:50%;background:var(--brand-red);flex:none}
  .watermark{position:absolute;border-radius:50%;background:var(--watermark)}
  .red-band{position:absolute;left:0;right:0;background:var(--brand-red)}

  /* Letterhead */
  .letterhead{left:48px;top:36px;width:499px;height:664px}
  .letterhead .brand{position:absolute;top:82px;left:0;right:0;justify-content:center;font-size:20px}
  .letterhead .brand-dot{width:16px;height:16px}
  .letterhead .watermark{width:230px;height:230px;left:134px;top:370px}
  .letterhead .footer{position:absolute;left:0;right:0;bottom:22px;text-align:center;font-size:7.5px;line-height:1.6}
  .letterhead .footer .web{font-size:9px;letter-spacing:.25em;color:var(--brand-navy);margin-top:2px}
  .letterhead .red-band{bottom:0;height:10px}

  /* Business card front */
  .card-front{left:595px;top:132px;width:245px;height:151px}
  .card-front .brand{position:absolute;top:38px;left:0;right:0;justify-content:center;font-size:12px}
  .card-front .brand-dot{width:10px;height:10px}
  .card-front .person{position:absolute;left:0;right:0;top:92px;text-align:center;font-size:7px;line-height:1.5}
  .card-front .person .name{color:var(--brand-red);font-weight:600;font-size:8.5px}
  .card-front .red-band{bottom:0;height:8px}

  /* Business card back */
  .card-back{left:869px;top:132px;width:242px;height:151px}
  .card-back .watermark{width:110px;height:110px;right:-14px;top:20px}
  .card-back .contact{position:absolute;left:14px;top:18px;font-size:6px;line-height:1.55}
  .card-back .contact p+p{margin-top:0}
  .card-back .gap{height:7px}
  .card-back .red-band{bottom:0;height:8px}

  /* Envelope */
  .envelope{left:566px;top:444px;width:540px;height:252px}
  .envelope .flap{position:absolute;left:0;right:0;top:0;height:56px;background:var(--brand-red)}
  .envelope .flap-edge{position:absolute;left:0;right:0;top:56px;height:4px;background:var(--brand-red-dark)}
  .envelope .flap .web{position:absolute;top:14px;left:0;right:0;text-align:center;color:#fff;font-size:7.5px;letter-spacing:.2em}
  .envelope .return{position:absolute;left:22px;top:102px}
  .envelope .return .brand{font-size:12px}
  .envelope .return .brand-dot{width:10px;height:10px}
  .envelope .return .addr{margin-top:8px;font-size:6px;line-height:1.55}
  .envelope .watermark{width:150px;height:150px;right:26px;top:82px}
</style>
</head>
<body>

<section class="sheet letterhead">
  <div class="brand"><span class="brand-dot"></span>Northwind Coastal</div>
  <div class="watermark" aria-hidden="true"></div>
  <div class="footer">
    <p>27340 SW Harrowgate Lane, Suite 240 | Kirkland, Washington 98471 | United States of America</p>
    <p>Toll Free: 1-800-555-0142 | Phone: 425-555-0187 | Fax: 425-555-0193</p>
    <p class="web">www.velorhaulers.example</p>
  </div>
  <div class="red-band"></div>
</section>

<section class="sheet card-front">
  <div class="brand"><span class="brand-dot"></span>Northwind Coastal</div>
  <div class="person">
    <p class="name">Tobin R. Lestrade</p>
    <p>President &amp;</p>
    <p>Chief Development Officer</p>
  </div>
  <div class="red-band"></div>
</section>

<section class="sheet card-back">
  <div class="watermark" aria-hidden="true"></div>
  <div class="contact">
    <p>27340 SW Harrowgate Lane, Suite 240</p>
    <p>Kirkland, Washington 98471</p>
    <p>United States of America</p>
    <div class="gap"></div>
    <p>Toll Free: 1-800-555-0142</p>
    <p>Phone: 425-555-0187</p>
    <p>Cell: 425-555-0164</p>
    <div class="gap"></div>
    <p>tlestrade@velorhaulers.example</p>
    <p>www.velorhaulers.example</p>
  </div>
  <div class="red-band"></div>
</section>

<section class="sheet envelope">
  <div class="flap"><p class="web">www.velorhaulers.example</p></div>
  <div class="flap-edge"></div>
  <div class="return">
    <div class="brand"><span class="brand-dot"></span>Northwind Coastal</div>
    <div class="addr">
      <p>27340 SW Harrowgate Lane, Suite 240</p>
      <p>Kirkland, Washington 98471</p>
      <p>United States of America</p>
    </div>
  </div>
  <div class="watermark" aria-hidden="true"></div>
</section>

</body>
</html>
```